Podcast Cover Design - Tiding For Level Heads

We renamed our podcast from the "Harborline Property Hour Podcast" to "Tidings For Level Heads" and we need a new podcast cover design, Instagram profile picture, and a YouTube banner.

More so we're looking for some sort of symbol/icon. Our old logo had the Cobalt Spire but we're moving to a much broader audience that isn't necessarily from Seattle and needs something that will appeal to them.

In the podcast, Doran reads the news that big media isn't covering including crime, business, homeless crisis, protests. We stay away from covering politics but our audience is mainly right-wing.

Attached are some additional designs we created in-house.

If we love the design we'll have additional job opportunities to create possible designs for merchandise.

Target Market(s)

80% Males aged 50+, Republican

Industry/Entity Type

News

Colors

Designer to choose colors to be used in the design.

Requirements
Must have
• OPEN TOO IDEAS
Nice to have
• OPEN TOO IDEAS
Should not have
• Cobalt Spire

```html
<!DOCTYPE html>
<html lang="en">
<head>
<meta charset="utf-8">
<title>Tidings For Level Heads — Podcast Cover</title>
<link href="https://fonts.googleapis.com/css2?family=Montserrat:wght@400;500;800&display=swap" rel="stylesheet">
<style>
  :root {
    --page-bg: #ffffff;
    --teal: #046e7a;
    --cream: #f8e3d4;
    --sage: #95ab8f;
    --band-blue: #4682a9;
  }
  html, body {
    margin: 0;
    padding: 0;
    width: 1200px;
    height: 1031px;
    overflow: hidden;
    background: var(--page-bg);
  }
  .cover {
    position: absolute;
    left: 230px;
    top: 145px;
    width: 741px;
    height: 741px;
    background: var(--teal);
    font-family: 'Montserrat', sans-serif;
    color: var(--cream);
  }
  .show-symbol {
    position: absolute;
    left: 267px;
    top: 73px;
    width: 206px;
    height: 231px;
    border-radius: 24px;
    background: radial-gradient(circle at 50% 45%, var(--cream) 0%, var(--cream) 55%, var(--sage) 100%);
  }
  .title {
    position: absolute;
    left: 0;
    width: 100%;
    top: 330px;
    margin: 0;
    text-align: center;
    font-weight: 800;
  }
  .title-lead {
    display: block;
    font-weight: 500;
    font-size: 46px;
    line-height: 52px;
    letter-spacing: 0.5px;
  }
  .title-main {
    display: block;
    font-size: 84px;
    line-height: 82px;
    letter-spacing: -1px;
  }
  .host-band {
    position: absolute;
    left: 0;
    top: 630px;
    width: 100%;
    height: 71px;
    background: var(--band-blue);
  }
  .host-badge {
    position: absolute;
    left: 79px;
    top: -11px;
    width: 78px;
    height: 78px;
    border-radius: 50%;
    background: var(--cream);
  }
  .host-badge svg {
    display: block;
  }
  .host-name {
    position: absolute;
    left: 179px;
    top: 0;
    line-height: 71px;
    font-size: 26px;
    font-weight: 500;
    letter-spacing: 0.3px;
    white-space: nowrap;
  }
</style>
</head>
<body>
  <div class="cover">
    <div class="show-symbol" role="img" aria-label="Podcast symbol: a hexagon of connected nodes around a small group of people with the word Podcast"></div>

    <h1 class="title">
      <span class="title-lead">TIDINGS FOR</span>
      <span class="title-main">LEVEL</span>
      <span class="title-main">HEADS</span>
    </h1>

    <div class="host-band">
      <div class="host-badge">
        <svg width="78" height="78" viewBox="0 0 78 78" aria-hidden="true">
          <rect x="31" y="14" width="16" height="34" rx="8" fill="var(--band-blue)"/>
          <path d="M24 38 v4 a15 15 0 0 0 30 0 v-4" fill="none" stroke="var(--band-blue)" stroke-width="4" stroke-linecap="round"/>
          <line x1="39" y1="57" x2="39" y2="66" stroke="var(--band-blue)" stroke-width="4" stroke-linecap="round"/>
        </svg>
      </div>
      <div class="host-name">WITH HOST DORAN CALLOWAY</div>
    </div>
  </div>
</body>
</html>
```